Travel Blogger Business Card for roamquill.net

I need a two-sided business card for a travel blogging website. The card should be both professional and fun at the same time. This is for the website www.roamquill.net

I don't necessarily think that the current logo on the website needs to be used on the business card but it can be. I am very flexible with ideas

Target Market(s)

Travel agencies that will be met at a conference.

Industry/Entity Type

Travel

Contact Information for Business Card

Company Name: Roam Quill.net
Name: Bertrand Olesky
Voice: +1-(345)-402-7731
Address: Coral Reach Shore, Grand Cayman, Cayman Islands
Email: ceo@roamquill.net

Colors
0592cd
0355a3
3176b5
33a6d7
85cae6
85acd3

Requirements
Must have
• Website address and name should be bigger than address, phone number, and email.

```html
<!DOCTYPE html>
<html lang="en">
<head>
<meta charset="utf-8">
<title>Roam Quill – Business Card</title>
<link href="https://fonts.googleapis.com/css2?family=PT+Sans:wght@400;700&family=PT+Serif&family=Roboto:wght@700&display=swap" rel="stylesheet">
<style>
  :root {
    --page: #e2e2e3;
    --grey-1: #929396;
    --grey-3: #bcbdbf;
    --grey-4: #d2d3d5;
    --grey-5: #e6e7e8;
    --grey-6: #f1f1f2;
    --ink: #1d1d1f;
    --ink-soft: #6d6e71;
    --blue-1: #0c56a4;
    --blue-2: #2a78b6;
    --blue-3: #1994d0;
    --blue-4: #2fa7d8;
    --blue-5: #85cae8;
    --white: #ffffff;
  }
  html, body {
    margin: 0;
    padding: 0;
    width: 1200px;
    height: 1000px;
    overflow: hidden;
    background: var(--page);
  }
  .canvas {
    position: relative;
    width: 1200px;
    height: 1000px;
  }
  .card {
    position: absolute;
    overflow: hidden;
  }
  .card-back {
    left: 459px;
    top: 102px;
    width: 621px;
    height: 373px;
    background: linear-gradient(90deg, var(--grey-4) 0%, var(--grey-5) 65%, var(--grey-6) 100%);
  }
  .card-back .surface-top {
    position: absolute;
    left: 0;
    top: 0;
    width: 621px;
    height: 190px;
    background: linear-gradient(90deg, var(--grey-1) 0%, var(--grey-3) 60%, var(--grey-5) 100%);
  }
  .card-back .surface-bottom {
    position: absolute;
    left: 0;
    top: 190px;
    width: 621px;
    height: 183px;
  }
  .card-front {
    left: 154px;
    top: 523px;
    width: 620px;
    height: 375px;
    background: linear-gradient(90deg, var(--blue-1) 0%, var(--blue-2) 35%, var(--blue-3) 60%, var(--blue-4) 82%, var(--blue-5) 100%);
  }
  .card-front .surface {
    position: absolute;
    inset: 0;
  }
  .identity {
    position: absolute;
    right: 84px;
    top: 108px;
    text-align: right;
    color: var(--ink);
  }
  .identity-name {
    font-family: "PT Sans", sans-serif;
    font-size: 21px;
    line-height: 25px;
  }
  .identity-name strong { font-weight: 700; }
  .identity-role {
    font-family: "PT Sans", sans-serif;
    font-size: 15px;
    line-height: 20px;
  }
  .identity-role .company {
    font-family: "PT Serif", serif;
    font-size: 14px;
  }
  .contact-list {
    position: absolute;
    left: 102px;
    top: 205px;
    margin: 0;
    padding: 0;
    list-style: none;
    font-family: "PT Sans", sans-serif;
    font-size: 17.5px;
    color: var(--ink-soft);
  }
  .contact-item {
    display: flex;
    align-items: center;
    height: 29.7px;
  }
  .contact-icon {
    width: 16px;
    height: 16px;
    margin-right: 16px;
    fill: var(--ink-soft);
  }
  .brand {
    position: absolute;
    left: 94px;
    top: 160px;
    display: flex;
    align-items: center;
    color: var(--white);
  }
  .brand-dot {
    width: 42px;
    height: 42px;
    border-radius: 50%;
    background: var(--white);
    margin-right: 18px;
  }
  .brand-name {
    font-family: "Roboto", sans-serif;
    font-weight: 700;
    font-size: 48px;
    letter-spacing: -0.5px;
    line-height: 1;
  }
</style>
</head>
<body>
<main class="canvas">

  <section class="card card-back" aria-label="Business card back">
    <div class="surface-top" role="img" aria-label="Grey layered stripe pattern"></div>
    <div class="surface-bottom" role="img" aria-label="Light grey layered stripe pattern"></div>

    <div class="identity">
      <div class="identity-name">Bertrand <strong>Olesky</strong></div>
      <div class="identity-role">CEO <span class="company">Roam Quill</span></div>
    </div>

    <ul class="contact-list">
      <li class="contact-item phone">
        <svg class="contact-icon" viewBox="0 0 16 16"><circle cx="8" cy="8" r="7" fill="none" stroke="var(--ink-soft)" stroke-width="1.4"/><path d="M5.3 4.4l1.3-.3.7 1.8-.8.7c.4.9 1 1.6 1.9 2l.7-.8 1.8.7-.3 1.3c-3 .2-5.5-2.4-5.3-5.4z"/></svg>
        +1-(345)-402-7731
      </li>
      <li class="contact-item email">
        <svg class="contact-icon" viewBox="0 0 16 16"><rect x="1.5" y="4" width="13" height="9" rx="0.5"/><path d="M1.8 4.4L8 9l6.2-4.6" fill="none" stroke="var(--grey-5)" stroke-width="1.2"/></svg>
        ceo@roamquill.net
      </li>
      <li class="contact-item web">
        <svg class="contact-icon" viewBox="0 0 16 16"><circle cx="8" cy="8" r="6.8" fill="none" stroke="var(--ink-soft)" stroke-width="1.4"/><ellipse cx="8" cy="8" rx="2.8" ry="6.8" fill="none" stroke="var(--ink-soft)" stroke-width="1.2"/><path d="M1.5 8h13M2.6 4.8h10.8M2.6 11.2h10.8" stroke="var(--ink-soft)" stroke-width="1.1"/></svg>
        www.roamquill.net
      </li>
      <li class="contact-item address">
        <svg class="contact-icon" viewBox="0 0 16 16"><path d="M8 1.2a4.6 4.6 0 0 0-4.6 4.6C3.4 9.3 8 14.8 8 14.8s4.6-5.5 4.6-9A4.6 4.6 0 0 0 8 1.2zm0 6.5a1.9 1.9 0 1 1 0-3.8 1.9 1.9 0 0 1 0 3.8z"/></svg>
        Coral Reach Shore, Grand Cayman, Cayman Islands
      </li>
    </ul>
  </section>

  <section class="card card-front" aria-label="Business card front">
    <div class="surface" role="img" aria-label="Blue layered stripe pattern"></div>
    <div class="brand">
      <span class="brand-dot" aria-hidden="true"></span>
      <span class="brand-name">ROAM QUILL</span>
    </div>
  </section>

</main>
</body>
</html>
```